Jewelry Manufacturing & Repair business needs advertising mailout - 9x4 flyer

Need new double sided flyer designed for an insert into a mailout. Want 9x4 (vertical design) to fit in 9.5" x 4.125" envelopes. Company based out of Louisiana called "Lem Tovick Manufacturing." Been in business for 45 years. We specialize in custom jewelry design and casting on the wholesale level. We are a full service trade shop offering CAD design, casting services, basic and advanced jewelry repair. Most of our customers are drawn to the fact that they talk directly with the owner/designer of the company each time they call. I've attached several images of CAD renders we've built and of our logo. I've also attached a copy of an old mailout we sent out 10 years ago that I designed myself (and it needed a lot of work). The business information listed in this old mailout is correct, except that we’ve been in business 45 years now. I would like the final design to be "business bold," portraying business strength and stability. I like shades of blue, or a gold/silver color scheme. Logo is black and white. Need double sided.

Looking for project to be less wordy than the 10 yr old mailout. Don’t need the “example scenario” in this flyer.
Updates

The weekend has made the 2 day timeframe very tight. Would like to extend timeframe, but I will select a design on Monday at 3:00 pm (USA Central time).

Target Market(s)

Retail Jewelry Stores

Industry/Entity Type

Jewelry

Colors
cfdeed
0455a3
3176b5
85acd3

Requirements
Must have
• All contact information.
Nice to have
• Purpose of this flyer is to get new accounts for our business. We want something that the retail jewelry store will notice something that will make them not throw away immediately, but instead hold onto for the future.
• This upcoming Christmas season is usually very busy for retail stores, so we can help take some of the overflow of work and still meet deadlines. With our help, they shouldn't have to turn any customer away.
Should not have
• We will be partnering in this mailout with a sister wholesale diamond company. Therefore, we don't want to mention that our company sells any diamonds, as we want to leave that part up to our sister company.

```html
<!DOCTYPE html>
<html lang="en">
<head>
<meta charset="utf-8">
<title>Lem Tovick Manufacturing – Trade Shop Flyer</title>
<link href="https://fonts.googleapis.com/css2?family=Cinzel:wght@400;600;700&family=Cormorant+Garamond:wght@500;600&family=Lora:wght@400;500&display=swap" rel="stylesheet">
<style>
  :root {
    --navy: #0c3a9c;
    --royal: #1448a8;
    --brand: #0455a3;
    --mid: #3176b5;
    --soft: #85acd3;
    --ice: #cfdeed;
    --band: #4f7fc6;
    --ink: #3a3a3a;
    --paper: #fbfbfc;
    --stage: #e6e9ee;
    --white: #ffffff;
  }
  * { box-sizing: border-box; margin: 0; padding: 0; }
  html, body { width: 1200px; height: 1200px; overflow: hidden; }
  body { background: var(--stage); position: relative; font-family: "Lora", Georgia, serif; }

  .flyer { position: absolute; top: 46px; width: 480px; height: 1080px; overflow: hidden; box-shadow: 0 6px 22px rgba(0,0,0,.22); }
  .flyer--front { left: 76px; background: var(--paper); }
  .flyer--back { left: 645px; background: linear-gradient(180deg, #0a2f8f 0%, var(--royal) 45%, #1a4fb0 100%); color: var(--white); }

  /* front */
  .front__hero { position: absolute; left: 0; top: 0; width: 228px; height: 322px; }
  .front__badge { position: absolute; left: 230px; top: 0; width: 196px; height: 198px; }
  .front__badge-name { position: absolute; left: 230px; top: 58px; width: 196px; text-align: center; font-family: "Cinzel", serif; font-weight: 600; font-size: 30px; line-height: 1.05; color: var(--white); }
  .front__title { position: absolute; left: 222px; top: 214px; width: 210px; text-align: center; font-family: "Cinzel", serif; font-weight: 400; font-size: 30px; line-height: 1.05; color: var(--ink); }
  .front__collage { position: absolute; left: 0; top: 250px; width: 480px; height: 730px; }
  .front__services { position: absolute; left: 0; top: 342px; width: 300px; height: 72px; }
  .front__services-text { position: absolute; left: 16px; top: 348px; font-family: "Cinzel", serif; font-size: 26px; line-height: 1.04; color: var(--white); }
  .front__phone { position: absolute; left: 0; top: 971px; width: 480px; height: 48px; background: var(--brand); color: var(--white); text-align: center; font-family: "Cormorant Garamond", serif; font-weight: 500; font-size: 40px; line-height: 48px; letter-spacing: 1px; }
  .front__address { position: absolute; left: 0; top: 1029px; width: 480px; text-align: center; font-family: "Cinzel", serif; font-size: 15px; color: var(--ink); }

  /* back */
  .back__hero { position: absolute; left: 0; top: 0; width: 480px; height: 396px; }
  .back__name-mark { position: absolute; left: 0; top: 54px; width: 480px; text-align: center; font-family: "Cinzel", serif; font-weight: 600; font-size: 34px; color: var(--white); }
  .back__name-mark::before { content: ""; display: block; width: 14px; height: 14px; margin: 0 auto 8px; background: var(--white); }
  .back__title { position: absolute; left: 0; top: 152px; width: 480px; text-align: center; font-family: "Cinzel", serif; font-weight: 700; font-size: 24px; text-shadow: 0 2px 3px rgba(0,0,0,.35); }
  .back__tagline { position: absolute; left: 0; top: 196px; width: 480px; text-align: center; font-family: "Cinzel", serif; font-size: 13px; letter-spacing: -.2px; }
  .back__intro { position: absolute; left: 30px; top: 266px; width: 420px; text-align: center; font-size: 14.2px; line-height: 19.8px; }
  .offer { position: absolute; left: 0; top: 396px; width: 480px; height: 159px; background: var(--band); text-align: center; }
  .offer__heading { display: flex; align-items: center; justify-content: center; gap: 12px; margin-top: 20px; font-family: "Cormorant Garamond", serif; font-weight: 600; font-size: 28px; letter-spacing: .5px; }
  .offer__heading::before, .offer__heading::after { content: ""; width: 80px; height: 1px; background: var(--ice); }
  .offer__list { list-style: none; margin-top: 4px; font-size: 14.4px; line-height: 19.6px; }
  .back__pitch { position: absolute; left: 14px; top: 582px; width: 452px; text-align: center; font-size: 14.6px; line-height: 19.2px; }
  .steps { position: absolute; left: 10px; top: 734px; width: 460px; display: flex; justify-content: space-between; }
  .step { width: 88px; text-align: center; font-size: 11px; line-height: 14.2px; color: var(--ice); }
  .step svg { display: block; margin: 0 auto 8px; }
  .contact { position: absolute; left: 0; top: 911px; width: 330px; height: 143px; }
  .contact__body { position: absolute; left: 16px; top: 918px; }
  .contact__heading { margin-left: 40px; font-family: "Cormorant Garamond", serif; font-weight: 600; font-size: 23px; }
  .contact__row { display: flex; align-items: center; gap: 14px; }
  .contact__phones { font-family: "Cormorant Garamond", serif; font-weight: 600; font-size: 27px; line-height: 26px; letter-spacing: 2.5px; }
  .contact__line { font-size: 14px; margin-top: 6px; }
  .seal { position: absolute; left: 350px; top: 920px; }
</style>
</head>
<body>

<!-- FRONT -->
<section class="flyer flyer--front">
  <svg class="front__hero" viewBox="0 0 228 322" role="img" aria-label="Ring render over a technical sketch of a three-stone engagement ring">
    <defs><radialGradient id="ringGlow" cx="45%" cy="72%" r="55%"><stop offset="0" stop-color="#c9ccd3"/><stop offset="1" stop-color="#fbfbfc"/></radialGradient></defs>
    <rect width="228" height="322" fill="url(#ringGlow)"/>
  </svg>

  <svg class="front__badge" viewBox="0 0 196 198"><polygon points="0,0 196,0 196,170 98,198 0,170" fill="var(--navy)"/></svg>
  <div class="front__badge-name">Lem<br>Tovick</div>

  <h1 class="front__title">Full Service<br>Trade Shop</h1>

  <svg class="front__collage" viewBox="0 250 480 730">
    <g role="img" aria-label="Torch melting metal in a crucible"><polygon points="292,358 480,258 480,542 388,562" fill="#5a3a26"/></g>
    <g role="img" aria-label="Oval halo ring render"><polygon points="88,426 288,358 384,558 176,646" fill="#c9ccd1"/></g>
    <g role="img" aria-label="Jeweler working at the bench"><polygon points="0,506 88,462 176,646 0,742" fill="#6b4a35"/></g>
    <polygon points="392,562 480,514 480,720" fill="var(--brand)"/>
    <g role="img" aria-label="Ring being polished on a wheel"><polygon points="192,658 396,562 480,722 480,762 312,849" fill="#9c8a7c"/></g>
    <g role="img" aria-label="Ring render beside CAD software on a monitor"><polygon points="24,754 192,658 280,842 140,886" fill="#8f99a6"/></g>
    <g role="img" aria-label="Close-up of a bezel set ring"><polygon points="312,849 480,762 480,970 356,970" fill="#b9bcc2"/></g>
  </svg>

  <svg class="front__services" viewBox="0 0 300 72"><polygon points="0,0 292,0 240,72 0,72" fill="var(--brand)"/></svg>
  <p class="front__services-text">Repair, Design,<br>&amp; Casting</p>

  <p class="front__phone">1-888-555-0142</p>
  <p class="front__address">12 Heron Lane Delhi, LA 71232</p>
</section>

<!-- BACK -->
<section class="flyer flyer--back">
  <svg class="back__hero" viewBox="0 0 480 396" role="img" aria-label="Blue-lit diamond with light streaks">
    <defs><radialGradient id="heroLight" cx="50%" cy="30%" r="70%"><stop offset="0" stop-color="#3f78d6"/><stop offset=".6" stop-color="#1446a8"/><stop offset="1" stop-color="#0a2f8f"/></radialGradient></defs>
    <rect width="480" height="396" fill="url(#heroLight)"/>
  </svg>

  <p class="back__name-mark">Lem Tovick</p>
  <h2 class="back__title">Lem Tovick Manufacturing</h2>
  <p class="back__tagline">Top Quality Craftsmanship, Friendly Personal Service</p>
  <p class="back__intro">We are a family operated business, serving the jewelry industry for over 45 years. Our experience provides us with a vast knowledge of the industry, as well as best practices for each unique item. We pride ourselves in quality craftsmanship with fast, honest, and courteous service.</p>

  <div class="offer">
    <h3 class="offer__heading">WHAT WE OFFER</h3>
    <ul class="offer__list">
      <li>Basic &amp; advanced jewelry repair</li>
      <li>Precision diamond setting</li>
      <li>CAD / CAM services for custom designs</li>
      <li>High quality gold, silver, &amp; platinum casting</li>
    </ul>
  </div>

  <p class="back__pitch">Lem Tovick Manufacturing can provide that highly skilled jeweler needed to take your business to the next level. We will work directly with you to meet all your customer’s needs, while maintaining a personal level of service that you will enjoy.<br>Our daily goal is to make you look good<br>to your customer!</p>

  <div class="steps">
    <div class="step">
      <svg width="52" height="52" viewBox="0 0 52 52" fill="none" stroke="#fff" stroke-width="2.5"><circle cx="26" cy="26" r="23"/><rect x="12" y="19" width="20" height="14"/><path d="M32 23h6l4 5v5H32"/><circle cx="18" cy="35" r="2.5"/><circle cx="36" cy="35" r="2.5"/></svg>
      You ship your item(s), with instructions for each job.
    </div>
    <div class="step">
      <svg width="52" height="52" viewBox="0 0 52 52" fill="none" stroke="#fff" stroke-width="2.5"><circle cx="26" cy="26" r="23"/><path d="M18 15c-2 0-4 2-3 5 2 7 7 13 14 16 3 1 5-1 5-3l-1-3-5-1-2 2c-3-1-6-4-7-7l2-2-1-5z"/></svg>
      We receive your items and give you a call with any questions or concerns
    </div>
    <div class="step">
      <svg width="52" height="52" viewBox="0 0 52 52" fill="none" stroke="#fff" stroke-width="2.5"><circle cx="26" cy="26" r="23"/><path d="M15 27l7 7 15-15"/></svg>
      Our Master Jewelers will provide the quality work
    </div>
    <div class="step">
      <svg width="52" height="52" viewBox="0 0 52 52" fill="none" stroke="#fff" stroke-width="2.5"><circle cx="26" cy="26" r="23"/><rect x="12" y="19" width="20" height="14"/><path d="M32 23h6l4 5v5H32"/><circle cx="18" cy="35" r="2.5"/><circle cx="36" cy="35" r="2.5"/></svg>
      We ship your items back to you via your preferred shipping method
    </div>
    <div class="step">
      <svg width="52" height="52" viewBox="0 0 52 52" fill="none" stroke="#fff" stroke-width="2.5"><circle cx="26" cy="26" r="23"/><rect x="15" y="18" width="22" height="17"/><path d="M15 24h22M26 18v17"/></svg>
      You receive the package, inspect the work, and finish the sale.
    </div>
  </div>

  <svg class="contact" viewBox="0 0 330 143"><polygon points="0,0 310,0 330,72 310,143 0,143" fill="var(--brand)"/></svg>
  <div class="contact__body">
    <p class="contact__heading">CONTACT US</p>
    <div class="contact__row">
      <svg width="26" height="26" viewBox="0 0 24 24" fill="#fff"><path d="M6.6 10.8a15 15 0 0 0 6.6 6.6l2.2-2.2c.3-.3.7-.4 1-.2 1.1.4 2.3.6 3.6.6.6 0 1 .4 1 1V20c0 .6-.4 1-1 1A17 17 0 0 1 3 4c0-.6.4-1 1-1h3.5c.6 0 1 .4 1 1 0 1.3.2 2.5.6 3.6.1.3 0 .7-.2 1z"/></svg>
      <p class="contact__phones">888-555-0142<br>318-555-0167</p>
    </div>
    <div class="contact__row contact__line">
      <svg width="26" height="24" viewBox="0 0 24 24" fill="#fff"><path d="M12 2a7 7 0 0 0-7 7c0 5 7 13 7 13s7-8 7-13a7 7 0 0 0-7-7zm0 9.5A2.5 2.5 0 1 1 12 6.5a2.5 2.5 0 0 1 0 5z"/></svg>
      <span>12 Heron Lane Delhi, LA 71232</span>
    </div>
    <div class="contact__row contact__line">
      <svg width="26" height="20" viewBox="0 0 24 18" fill="#fff"><path d="M1 1h22v16H1z" fill="none" stroke="#fff" stroke-width="2"/><path d="M1 2l11 8 11-8v3l-11 8L1 5z"/></svg>
      <span>sales@lemtovickmfg.com</span>
    </div>
  </div>

  <svg class="seal" width="110" height="140" viewBox="0 0 110 140">
    <polygon points="30,80 14,132 34,124 44,138 56,92" fill="#c9ccd3"/>
    <polygon points="80,80 96,132 76,124 66,138 54,92" fill="#c9ccd3"/>
    <circle cx="55" cy="54" r="52" fill="#c2c6cd"/>
    <circle cx="55" cy="54" r="44" fill="#30384a"/>
  </svg>
</section>

</body>
</html>
```